Vell Expertline home page

I want a new look and design for the home page of www.vellexpertline.example . Something new that better shows what our service is about. We provide live technical support to RE professionals via our smart phone app and website. The service is available for home inspectors, appraisers, real estate agents and others in the Real Estate Profession.

I just want a great looking home page design that demonstrates the service. Does not have to be a functional site, just the design.

Imagine walking around or through a house and having a technical question during your inspection. You pull out your phone, open the Vell Exp app and select a category, type in your question and it opens your camera to attach a photo. You submit your question and experts review it and send you an answer within minutes. Possibly while you are still on the job.
Updates

I am really looking for a way to convey that our service is all about RE professionals, like home inspectors, appraisers, RE agents getting help while they are in the field at the homes they are working at.   A home inspector looks at an electrical panel snaps a picture and sends their question to us and they get a response before they even leave the jobsite.  That feeling.

Reason: I would like to see the designs convey the feeling that our service is something every professional needs while doing their jobs. We have hundreds of inspectors using our service to get fast answers to very technical questions using our smart phone app.

Target Market(s)

Home Inspectors, Real Estate Appraisers, Real Estate Agents

Industry/Entity Type

Real Estate

Colors

Designer to choose colors to be used in the design.

Requirements
Must have
• People must understand we provide experts who respond to their real estate related technical support questions using our patent pending smart phone app.

```html
<!DOCTYPE html>
<html lang="en">
<head>
<meta charset="utf-8">
<title>Vell Expertline – Features</title>
<link rel="stylesheet" href="https://fonts.googleapis.com/css2?family=Questrial&family=Source+Sans+3:wght@400;600&display=swap">
<style>
  :root {
    --page-bg: #f6f7f9;
    --accent-line: #2c9ad6;
    --ink: #1f1f1f;
    --heading: #2a2a2a;
    --green: #9bc31c;
    --hero-strip: #d9dadc;
    --device-red: #e45a60;
    --device-dark: #141414;
    --screen-blue: #4a86c0;
  }
  * { margin: 0; padding: 0; box-sizing: border-box; }
  html, body { width: 1200px; height: 532px; overflow: hidden; }
  body {
    position: relative;
    background: var(--page-bg);
    font-family: "Source Sans 3", sans-serif;
    color: var(--ink);
  }
  .top-rule {
    position: absolute; left: 0; top: 0; width: 1200px; height: 2px;
    background: var(--accent-line);
  }
  .hero-edge {
    position: absolute; left: 317px; top: 0; width: 562px; height: 2px;
    background: var(--hero-strip);
  }
  .section-title {
    position: absolute; left: 0; top: 80px; width: 1200px;
    text-align: center;
    font-family: "Questrial", sans-serif; font-weight: 400;
    font-size: 30px; line-height: 38px; color: var(--heading);
  }
  .section-intro {
    position: absolute; left: 0; top: 144px; width: 1200px;
    text-align: center; font-size: 14px; line-height: 23px;
  }
  .feature {
    position: absolute; width: 260px; font-size: 14px; line-height: 23px;
  }
  .feature h3 { font-size: 14px; font-weight: 600; color: var(--green); }
  .feature--left { text-align: right; left: 166px; }
  .feature--right { text-align: left; left: 769px; }
  .row-1 { top: 259px; }
  .row-2 { top: 396px; }
  .app-preview {
    position: absolute; left: 480px; top: 213px; width: 238px; height: 319px;
    border-radius: 36px 36px 0 0;
    background: linear-gradient(180deg, var(--device-dark) 0%, #2a3b52 45%, var(--screen-blue) 100%);
    border: 5px solid var(--device-red);
    border-bottom: none;
  }
</style>
</head>
<body>
  <div class="top-rule"></div>
  <div class="hero-edge"></div>

  <h2 class="section-title">Awesome features</h2>
  <p class="section-intro">Epsum factorial non deposit quid pro quo hic escorol.<br>Olypian quarrels et gorilla congolium sic.</p>

  <div class="feature feature--left row-1">
    <h3>Lorem ipsum dolor</h3>
    <p>Epsum factorial non deposit<br>quid pro quo hic&nbsp; factorial non<br>deposit quid pro quo hic</p>
  </div>
  <div class="feature feature--left row-2">
    <h3>Lorem ipsum dolor</h3>
    <p>Epsum factorial non deposit<br>quid pro quo hic escorol.</p>
  </div>
  <div class="feature feature--right row-1">
    <h3>Lorem ipsum dolor</h3>
    <p>Epsum factorial non deposit<br>quid pro q factorial non deposit<br>quid pro quo hic&nbsp; factorial non</p>
  </div>
  <div class="feature feature--right row-2">
    <h3>Lorem ipsum dolor</h3>
    <p>Epsum factorial non deposit<br>quid pro quo hic escorol.</p>
  </div>

  <div class="app-preview" role="img" aria-label="Red smartphone showing the Vell Exp app screen where a question about an electrical panel is entered, photos attached and submitted"></div>
</body>
</html>
```